Landing Page Design for Business Page

I need a very attractive landing page designed for my business to obtain customer information. I would like an improvement to an existing landing page we have that is much more appealing and modern.

I have included resources and assets in the below Google Drive folder. I am a big fan of some of the imagery in the "Banners" folder for design.

https://files.qorvintstore.net/shared/8kTwp31XnaLmQe0Vhz-4YcRbu7JsOdfG?mode=view

Here is existing landing page that I would like improved upon.

http://lp4.vemtrapower.com/vmx-lp-signup

```html
<!DOCTYPE html>
<html lang="en">
<head>
<meta charset="utf-8">
<title>Vemtra Power – Home Energy Efficiency</title>
<link href="https://fonts.googleapis.com/css2?family=Montserrat:wght@400;500;600;700;800&family=Poppins:wght@400;500;600&display=swap" rel="stylesheet">
<style>
:root{
  --teal-900:#0c3f5a;
  --teal-800:#12506f;
  --teal-700:#1a6283;
  --teal-600:#23739a;
  --navy:#123a66;
  --green:#3fae49;
  --ink:#1f2a33;
  --muted:#4a5660;
  --paper:#ffffff;
  --card:#f8f4f1;
  --grey-bg:#efefef;
}
*{margin:0;padding:0;box-sizing:border-box}
html,body{width:1200px;height:4505px;overflow:hidden}
body{font-family:"Poppins",sans-serif;color:var(--ink);background:var(--paper);position:relative}
.abs{position:absolute}
a{color:inherit;text-decoration:none}

/* header + hero */
.hero-bg{left:0;top:0;width:1200px;height:730px}
.brand{left:42px;top:6px;width:105px;height:44px;background:#fff;display:flex;align-items:center;justify-content:center;gap:6px;font-family:"Montserrat",sans-serif;font-weight:700;font-size:12px;color:var(--teal-800);white-space:nowrap}
.brand .dot{width:9px;height:9px;border-radius:50%;background:var(--teal-800);flex:none}
.social{display:flex;gap:8px}
.social span{width:16px;height:16px;border-radius:50%;background:#fff;display:block}
.search{left:1050px;top:21px;width:108px;height:21px;border:1px solid #cfe3ee;border-radius:11px}
.search span{position:absolute;left:12px;top:3px;font-size:8px;color:#a9c7d6}
.hero-title{left:42px;top:172px;width:480px;font-family:"Montserrat",sans-serif;font-weight:800;font-size:36px;line-height:45px;color:#fff}
.hero-sub{left:42px;top:377px;width:440px;font-family:"Montserrat",sans-serif;font-size:18px;line-height:24px;color:#fff}
.btn-outline{left:42px;top:451px;width:89px;height:35px;background:#fff;color:var(--ink);font-size:12px;font-family:"Montserrat",sans-serif;font-weight:600;display:flex;align-items:center;justify-content:center;gap:6px}
.form-panel{left:616px;top:119px;width:399px;height:472px;background:rgba(120,128,132,.82);border-radius:8px}
.form-panel h2{position:absolute;left:21px;top:24px;width:370px;font-family:"Montserrat",sans-serif;font-weight:700;font-size:24px;line-height:29px;color:#fff}
.field{position:absolute;left:21px;width:344px;height:31px;background:#fff;font-size:11px;color:#888;padding-left:26px;display:flex;align-items:center}
.field.phone{padding-left:14px;gap:10px}
.field.phone .flag{width:36px;height:14px;background:linear-gradient(#c8323c 0 15%,#fff 15% 30%,#c8323c 30% 45%,#fff 45% 60%,#c8323c 60% 75%,#fff 75% 90%,#c8323c 90%);position:relative}
.field.phone .flag::before{content:"";position:absolute;left:0;top:0;width:15px;height:8px;background:#2a3f8f}
.submit{position:absolute;left:21px;top:413px;width:129px;height:31px;background:#0e1e2a;color:#fff;font-size:12px;font-family:"Montserrat",sans-serif;font-weight:600;display:flex;align-items:center;justify-content:center}

/* section headings: centred on their left coordinate, single line */
.sec-head{position:absolute;transform:translateX(-50%);white-space:nowrap;text-align:center;font-family:"Poppins",sans-serif;font-weight:500;font-size:34px;line-height:40px}
.sec-head::after{content:"";display:block;margin:4px auto 0;width:100%;height:2px;background:currentColor}
.sec-head.light{color:#fff}
.sec-head.dark{color:var(--ink)}

/* about */
.about-ring{left:186px;top:782px}
.about-text{left:708px;top:848px;width:385px;font-family:"Montserrat",sans-serif;font-size:17px;line-height:25px;color:var(--ink)}
.about-text p+p{margin-top:10px}
.btn-solid{background:var(--navy);color:#fff;font-size:13px;font-family:"Montserrat",sans-serif;display:flex;align-items:center;justify-content:center;border-radius:2px}

/* services */
.band{left:0;width:1200px}
.service-card{width:256px;height:358px;background:var(--card);top:1368px}
.service-card .photo{width:256px;height:166px;display:block}
.service-card h3{position:absolute;left:22px;top:180px;font-family:"Montserrat",sans-serif;font-size:12px;font-weight:700}
.service-card p{position:absolute;left:22px;top:210px;width:205px;font-family:"Montserrat",sans-serif;font-size:12px;line-height:16px}
.service-card .more{position:absolute;right:16px;top:336px;font-family:"Montserrat",sans-serif;font-size:11.5px;font-weight:500}

/* how we work */
.intro{left:245px;top:1957px;width:710px;text-align:center;font-family:"Montserrat",sans-serif;font-size:14.5px;line-height:20px}
.step-title{top:2055px;width:220px;text-align:center;font-family:"Montserrat",sans-serif;font-size:18px;line-height:28px;font-weight:500}
.step-text{top:2360px;font-family:"Montserrat",sans-serif;font-size:9.4px;line-height:14.8px;color:var(--ink)}

/* gallery */
.g-photo{top:2711px;height:152px;border:3px solid #fff}

/* covid */
.covid-text{left:647px;top:3126px;width:495px;font-family:"Montserrat",sans-serif;font-size:13.5px;line-height:19.5px}
.covid-text p+p{margin-top:6px}
.covid-text .tel{color:#2a6ab3}

/* cta */
.cta-title{left:300px;top:3595px;width:600px;text-align:center;color:#fff;font-family:"Poppins",sans-serif;font-size:28px;line-height:44px}
.btn-green{left:540px;top:3734px;width:118px;height:27px;background:var(--green);color:#fff;border-radius:14px;font-size:15px;display:flex;align-items:center;justify-content:center}

/* testimonial */
.quote{left:250px;top:4110px;width:700px;text-align:center;font-family:"Montserrat",sans-serif;font-size:17px;line-height:25px}
.dots{left:556px;top:4238px;display:flex;gap:13px}
.dots span{width:7px;height:7px;border-radius:50%;background:var(--ink)}

/* footer */
.footer-brand{left:42px;top:4300px;font-family:"Montserrat",sans-serif;font-weight:700;font-size:22px;color:#fff;display:flex;align-items:center;gap:8px}
.footer-brand .dot{width:12px;height:12px;border-radius:50%;background:#fff}
.footer-blurb{left:42px;top:4346px;width:230px;font-family:"Montserrat",sans-serif;font-size:9px;line-height:13px;color:#fff}
.f-col h4{font-family:"Montserrat",sans-serif;font-weight:800;font-size:23px;color:#fff;margin-bottom:16px;white-space:nowrap}
.f-col ul{list-style:none;font-family:"Montserrat",sans-serif;font-size:11px;color:#fff}
.f-col li{height:22.5px}
.f-col li::before{content:"•";margin-right:8px}
.contact-item{display:flex;align-items:flex-start;gap:12px;font-family:"Montserrat",sans-serif;font-size:11px;line-height:15px;color:#fff;position:absolute}
.copy{left:0;top:4488px;width:1200px;height:17px;background:var(--teal-900);color:#fff;font-size:10px;text-align:center;line-height:17px}
</style>
</head>
<body>

<!-- HERO -->
<svg class="abs hero-bg" viewBox="0 0 1200 730" role="img" aria-label="Photo of insulation crew beside a branded service van, deep teal overlay">
  <defs>
    <linearGradient id="heroGrad" x1="0" y1="0" x2="1" y2="1">
      <stop offset="0" stop-color="#0e4a68"/>
      <stop offset=".55" stop-color="#1b6285"/>
      <stop offset="1" stop-color="#2c7799"/>
    </linearGradient>
  </defs>
  <path d="M0 0H1200V545C1120 530 1060 590 1000 630C930 680 860 680 780 660C700 640 620 700 520 715C400 730 330 690 260 640C200 600 150 550 80 555C40 558 20 565 0 570Z" fill="url(#heroGrad)"/>
  <path d="M520 715C620 700 700 640 780 660C700 660 620 720 520 725Z" fill="#c9d9de" opacity=".6"/>
</svg>

<div class="abs brand"><span class="dot"></span>Vemtra Power</div>

<nav class="abs" style="left:262px;top:24px;width:635px;height:26px;border-bottom:1px solid rgba(255,255,255,.75);font-family:Montserrat,sans-serif;font-size:12px;color:#fff">
  <a class="abs" style="left:0;top:0">HOME</a>
  <a class="abs" style="left:93px;top:0">SERVICES</a>
  <a class="abs" style="left:214px;top:0">REABTES</a>
  <a class="abs" style="left:329px;top:0">ABOUT US</a>
  <a class="abs" style="left:443px;top:0">COVID-19</a>
  <a class="abs" style="left:564px;top:0">EMPLOYEES</a>
</nav>
<div class="abs social" style="left:931px;top:23px"><span></span><span></span><span></span><span></span></div>
<div class="abs search"><span>search</span></div>

<h1 class="abs hero-title">We can help you save on your energy bills by improving your energy efficiency</h1>
<p class="abs hero-sub">Contact Vemtra Power for a no-cost, no-obligation estimate today</p>
<a class="abs btn-outline">EXPLORE <svg width="7" height="10" viewBox="0 0 7 10"><path d="M1 1l4 4-4 4" stroke="#1f2a33" stroke-width="1.6" fill="none"/></svg></a>

<form class="abs form-panel">
  <h2>Do I qualify for 75-100% off insulation &amp; weatherization?</h2>
  <div class="field" style="top:114px">First Name</div>
  <div class="field" style="top:177px">Last Name</div>
  <div class="field phone" style="top:240px"><span class="flag"></span>(+1)555-0123</div>
  <div class="field" style="top:303px">Email Address</div>
  <div class="field" style="top:365px">City</div>
  <div class="submit">SUBMIT FORM</div>
</form>

<!-- ABOUT -->
<h2 class="sec-head dark" style="left:861px;top:772px">About Us</h2>
<svg class="abs about-ring" width="350" height="340" viewBox="0 0 350 340">
  <defs><radialGradient id="aboutGrad" cx=".5" cy=".45" r=".6"><stop offset="0" stop-color="#c9a26f"/><stop offset=".55" stop-color="#7d5a36"/><stop offset="1" stop-color="#3a2816"/></radialGradient></defs>
  <path d="M70 290A166 166 0 0 1 175 14" stroke="var(--teal-800)" stroke-width="5" fill="none"/>
  <circle cx="185" cy="168" r="160" fill="url(#aboutGrad)" role="img" aria-label="Technician in green shirt spraying insulation in an attic"/>
</svg>
<div class="abs about-text">
  <p>Lorem ipsum dolor sit amet, consectetur adipiscing elit. Id dignissim diam adipiscing laoreet vulputate rhoncus.</p>
  <p>Lorem ipsum dolor sit amet, consectetur adipiscing elit. Est, amet molestie purus vitae lacus. Congue viverra tellus nibh posuere pharetra sit fames est.</p>
</div>
<a class="abs btn-solid" style="left:711px;top:1063px;width:90px;height:35px">Learn More</a>

<!-- SERVICES -->
<div class="abs band" style="top:1219px;height:556px;background:linear-gradient(135deg,var(--teal-800),var(--teal-700) 60%,#2a6f8e)" role="img" aria-label="Faded photo of a service van and crew behind a teal overlay"></div>
<h2 class="sec-head light" style="left:600px;top:1297px">Services</h2>

<article class="abs service-card" style="left:170px">
  <div class="photo" role="img" aria-label="Two technicians unloading an insulation hose reel" style="background:linear-gradient(135deg,#3d4b45,#6f8a6c 55%,#2f3a36)"></div>
  <h3>Home Energy Assessments</h3>
  <p>Lorem ipsum dolor sit amet, consectetur adipiscing elit. Phasellus morbi amet eu morbi sapien consequat magna tellus tellus.</p>
  <span class="more">Read More ›</span>
</article>
<article class="abs service-card" style="left:472px">
  <div class="photo" role="img" aria-label="Technician in respirator sealing an attic floor" style="background:linear-gradient(135deg,#6b4a2e,#a3794d 55%,#4a3320)"></div>
  <h3>Insulation &amp; Air Sealing</h3>
  <p>Lorem ipsum dolor sit amet, consectetur adipiscing elit. Phasellus morbi amet eu morbi sapien consequat magna tellus tellus.</p>
  <span class="more">Read More ›</span>
</article>
<article class="abs service-card" style="left:775px">
  <div class="photo" role="img" aria-label="Technician in green shirt working with an insulation hose" style="background:linear-gradient(135deg,#8a6238,#c79a5f 55%,#5f4226)"></div>
  <h3>Virtual Assessments</h3>
  <p>Lorem ipsum dolor sit amet, consectetur adipiscing elit. Phasellus morbi amet eu morbi sapien consequat magna tellus tellus.</p>
  <span class="more">Read More ›</span>
</article>

<!-- HOW WE WORK -->
<h2 class="sec-head dark" style="left:600px;top:1888px">How We Work</h2>
<p class="abs intro">Lorem ipsum dolor sit amet, consectetur adipiscing elit. Phasellus morbi amet eu morbi sapien consequat magna tellus tellus.Lorem ipsum dolor sit amet, consectetur adipiscing elit. Phasellus morbi amet eu morbi sapien consequat magna tellus tellus.</p>

<div class="abs step-title" style="left:252px">PERFORM<br>IN-HOME AUDIT</div>
<div class="abs step-title" style="left:462px">GAIN<br>YOUR APPROVAL</div>
<div class="abs step-title" style="left:723px">IMPROVE ENERGY<br>EFFICIENCY</div>

<svg class="abs" style="left:0;top:0" width="1200" height="2600" viewBox="0 0 1200 2600">
  <defs>
    <linearGradient id="ring" x1="0" y1="0" x2="1" y2="1"><stop offset="0" stop-color="#3fae49"/><stop offset="1" stop-color="#1f9fb8"/></linearGradient>
  </defs>
  <g fill="none" stroke="var(--navy)" stroke-width="3.5">
    <path d="M422 2148A108 108 0 1 0 467 2225C475 2160 510 2123 565 2122A108 108 0 0 1 672 2178"/>
    <path d="M486 2270A108 108 0 0 0 689 2230C700 2165 740 2118 800 2117A108 108 0 1 1 736 2303"/>
  </g>
  <g fill="var(--navy)">
    <circle cx="422" cy="2148" r="6"/><circle cx="672" cy="2178" r="6"/>
    <circle cx="486" cy="2270" r="6"/><circle cx="736" cy="2303" r="6"/>
  </g>
  <g>
    <circle cx="359" cy="2225" r="52" fill="#fff" stroke="url(#ring)" stroke-width="6"/>
    <circle cx="359" cy="2225" r="40" fill="#f3f5f7" role="img" aria-label="Energy gauge with technician icon"/>
    <circle cx="581" cy="2230" r="52" fill="#fff" stroke="url(#ring)" stroke-width="6"/>
    <rect x="558" y="2230" width="9" height="20" fill="#2f7fd1"/>
    <rect x="571" y="2218" width="9" height="32" fill="#2f7fd1"/>
    <rect x="584" y="2206" width="9" height="44" fill="#2f7fd1"/>
    <rect x="597" y="2196" width="9" height="54" fill="#2f7fd1"/>
    <path d="M552 2245L575 2226 590 2232 612 2204" stroke="#f2a23a" stroke-width="3" fill="none"/>
    <circle cx="805" cy="2225" r="52" fill="#fff" stroke="url(#ring)" stroke-width="6"/>
    <circle cx="805" cy="2225" r="40" fill="#f3f5f7" role="img" aria-label="Efficient house with solar panel and lightbulb icon"/>
  </g>
</svg>

<p class="abs step-text" style="left:268px;width:172px">We begin our journey with you by performing an in-home audit. A member of our team, a fully qualified technician, will schedule a time that works for you to come and assess your home. The assessment will include various tests to decide how best to make your home more energy-efficient.</p>
<p class="abs step-text" style="left:470px;width:222px">Following the in-home audit, Vemtra Power will provide you with a written evaluation of how your home's energy efficiency can be improved. In that evaluation, we will include the cost after any incentives or discounts that you are eligible for, and a form to confirm whether you would like to work with us to improve your home's energy efficiency using insulation and weatherization tools.</p>
<p class="abs step-text" style="left:717px;width:250px">After receiving your request to start work, a member of our team will contact you to schedule the work appointment. Our team will perform the work agreed upon in the evaluation, and leave your home more energy efficient!</p>

<!-- GALLERY -->
<div class="abs band" style="top:2583px;height:361px;background:linear-gradient(135deg,var(--teal-800),var(--teal-700) 60%,#2a6f8e)" role="img" aria-label="Faded photo of service trucks behind a teal overlay"></div>
<h2 class="sec-head light" style="left:600px;top:2651px">Gallery</h2>
<div class="abs g-photo" style="left:66px;width:242px;background:linear-gradient(135deg,#4fae3f,#cfd7d9 55%,#6a6f6a)" role="img" aria-label="Crew unloading a green truck at a garage"></div>
<div class="abs g-photo" style="left:341px;width:241px;background:linear-gradient(135deg,#c9c3b5,#7c8a80 55%,#3f4a44)" role="img" aria-label="Technician working inside a truck cargo area"></div>
<div class="abs g-photo" style="left:621px;width:234px;background:linear-gradient(135deg,#5b8f4a,#3c9a55 55%,#c8c4b8)" role="img" aria-label="Branded green box truck parked on a street"></div>
<div class="abs g-photo" style="left:894px;width:234px;background:linear-gradient(135deg,#d7d3cb,#4ea865 55%,#45403b)" role="img" aria-label="Crew member beside an open truck liftgate"></div>

<!-- COVID -->
<svg class="abs" style="left:150px;top:3005px" width="340" height="330" viewBox="0 0 340 330">
  <defs><radialGradient id="covidGrad" cx=".5" cy=".5" r=".6"><stop offset="0" stop-color="#3a9b5a"/><stop offset=".5" stop-color="#8b6a48"/><stop offset="1" stop-color="#3b2a1c"/></radialGradient></defs>
  <path d="M88 23A158 158 0 0 0 88 298" stroke="var(--navy)" stroke-width="4" fill="none"/>
  <circle cx="88" cy="23" r="6" fill="var(--navy)"/><circle cx="88" cy="298" r="6" fill="var(--navy)"/>
  <circle cx="168" cy="162" r="150" fill="url(#covidGrad)" role="img" aria-label="Technician wearing a respirator in an attic"/>
</svg>
<h2 class="sec-head dark" style="left:772px;top:3050px">Covid-19 Notice</h2>
<div class="abs covid-text">
  <p>The wellbeing of our customers and employees is of the utmost importance to us. Due to the COVID-19 social distancing guidelines, all HomeCrest employees who visit customer's home will be equipped with personal protective equipment and will limit in-home time as much as possible.</p>
  <p>Have specific questions regarding our safety precautions? Fill out the form on our Contact page or give us a call at <span class="tel">(781) 555 – 0142.</span></p>
</div>

<!-- CTA -->
<div class="abs band" style="top:3402px;height:455px;background:linear-gradient(180deg,#3a3530,#4e3f36 45%,#2d2a27)" role="img" aria-label="Brick colonial house with trees, darkened"></div>
<svg class="abs" style="left:44px;top:3638px" width="20" height="36" viewBox="0 0 20 36"><path d="M17 2L3 18l14 16" stroke="#fff" stroke-width="2" fill="none"/></svg>
<svg class="abs" style="left:1138px;top:3638px" width="20" height="36" viewBox="0 0 20 36"><path d="M3 2l14 16L3 34" stroke="#fff" stroke-width="2" fill="none"/></svg>
<p class="abs cta-title">Get your&nbsp; FREE&nbsp; home energy saving estimate today!</p>
<a class="abs btn-green">contact us</a>

<!-- TESTIMONIAL -->
<div class="abs band" style="top:3857px;height:416px;background:var(--grey-bg)"></div>
<h2 class="sec-head dark" style="left:600px;top:3933px">Testimonial</h2>
<div class="abs" style="left:556px;top:4008px;width:88px;height:88px;border-radius:50%;background:linear-gradient(180deg,#d9d9d9,#6f6f6f)" role="img" aria-label="Customer portrait"></div>
<p class="abs quote">Lorem ipsum dolor sit amet, consectetur adipiscing elit.<br>Amet faucibus amet ipsum mattis aliquet sed porta dapibus nullam.<br>Adipiscing id sit interdum ut pretium ut porta vel.</p>
<div class="abs dots"><span></span><span></span><span></span><span></span><span></span></div>

<!-- FOOTER -->
<footer class="abs band" style="top:4273px;height:215px;background:var(--teal-700)"></footer>
<div class="abs footer-brand"><span class="dot"></span>Vemtra Power</div>
<p class="abs footer-blurb">Lorem ipsum dolor sit amet, consectetur adipiscingelit.Elementum nulla enim vel aliquam etiam lectus quam. Pellentesque vestibulum et, felis, senuncrisus.Elementum aliquam etiam lectus quam.</p>
<div class="abs social" style="left:42px;top:4440px"><span></span><span></span><span></span><span></span></div>

<div class="abs f-col" style="left:423px;top:4290px">
  <h4>QUICK LINKS</h4>
  <ul><li>Home</li><li>ABOUT</li><li>LOCATON</li><li>FAQ</li><li>SHIPPING</li></ul>
</div>
<div class="abs f-col" style="left:707px;top:4290px">
  <h4>PRODUCT</h4>
  <ul><li>OUR STORY</li><li>OUR VALUES</li><li>OUR MISSION</li><li>OUR BLOG</li></ul>
</div>
<div class="abs f-col" style="left:957px;top:4290px"><h4>CONTACT US</h4></div>
<div class="contact-item" style="left:968px;top:4340px">
  <svg width="14" height="14" viewBox="0 0 24 24"><path d="M6.6 10.8a15 15 0 006.6 6.6l2.2-2.2a1 1 0 011-.25 11.4 11.4 0 003.6.57 1 1 0 011 1V20a1 1 0 01-1 1A17 17 0 013 4a1 1 0 011-1h3.5a1 1 0 011 1 11.4 11.4 0 00.57 3.6 1 1 0 01-.25 1z" fill="#fff"/></svg>
  <span>774-555-0187</span>
</div>
<div class="contact-item" style="left:968px;top:4378px">
  <svg width="16" height="12" viewBox="0 0 16 12"><rect x="0" y="0" width="16" height="12" fill="#fff"/><path d="M0 0l8 6 8-6" stroke="#1a6283" stroke-width="1.4" fill="none"/></svg>
  <span>info@vemtrapower.com</span>
</div>
<div class="contact-item" style="left:968px;top:4412px">
  <svg width="14" height="18" viewBox="0 0 14 18"><path d="M7 0a7 7 0 017 7c0 5-7 11-7 11S0 12 0 7a7 7 0 017-7z" fill="#fff"/><circle cx="7" cy="7" r="2.6" fill="#1a6283"/></svg>
  <span>42 Harbor Lane, Suite 5,<br>Fairhaven, MA 02719</span>
</div>
<div class="abs copy">Vemtra Power © 2021 All rights reserved.</div>

</body>
</html>
```